Coffee House With Cycling Theme Wants Business Cards

We want to create a business card for a coffee house that has a cycling theme. We expect to use the current logo on one side of the business card and we have been considering adding the words 'COFFEE HOUSE' underneath (see example). For the other side of the business card we want an interesting design with tag-line, address and social media links (the normal business card stuff). See examples provided but we are not fixed on having it exactly as shown, we are very open to great creative ideas. Please note our logo has the initials ‘RV' in orange embedded in the design and this must be retained. However, you can play with the words COFFEE HOUSE as well as use the orange color on the backside of the business card, as you see fit. For an image on the backside of the business card it can be a photo, hand-drawn or whatever but it must visually combine coffee and cycling in some way. The interior of the Coffee House will be reclaimed wood, rustic and have an urban feel to it with cycling artifacts hanging from the walls/ceiling, etc. Finally, it would be beneficial if the business card design elements can be easily used on flyers and other promotional assets. Good luck, we are looking forward to seeing your creative ideas.

Target Market(s)

Coffee lovers and cycling fans

Contact Information for Business Card

See project description.

Colors

Designer to choose colors to be used in the design.

Requirements
Must have
• Must use the current logo provided and combine a coffee and bike theme.
Nice to have
• Orange is used in current logo and could be used as an accent color on the backside of the business card.

```html
<!DOCTYPE html>
<html lang="en">
<head>
<meta charset="utf-8">
<title>RV Coffee House – Business Card Back</title>
<link href="https://fonts.googleapis.com/css2?family=Parisienne&family=Libre+Baskerville&display=swap" rel="stylesheet">
<style>
  :root {
    --card-orange: #f0652a;
    --ink: #3b3b3b;
    --script-white: #ffffff;
    --photo-light: #b8773a;
    --photo-dark: #4a2a1c;
    --shadow: rgba(90, 30, 5, 0.5);
  }
  * { margin: 0; padding: 0; box-sizing: border-box; }
  html, body { width: 1200px; height: 686px; overflow: hidden; background: var(--card-orange); }
  .card {
    position: relative;
    width: 1200px;
    height: 686px;
    background: var(--card-orange);
    overflow: hidden;
    font-family: "Libre Baskerville", Georgia, serif;
    color: var(--ink);
  }
  .photo-placeholder {
    position: absolute;
    left: 920px;
    top: 32px;
    width: 626px;
    height: 626px;
    border-radius: 50%;
    background: radial-gradient(circle at 60% 45%, var(--photo-light) 0%, var(--photo-dark) 100%);
    box-shadow: -24px 8px 50px var(--shadow);
  }
  .tagline {
    position: absolute;
    left: 172px;
    top: 138px;
    font-family: "Parisienne", cursive;
    font-size: 82px;
    line-height: 1.2;
    color: var(--script-white);
    white-space: nowrap;
  }
  .contact {
    position: absolute;
    left: 330px;
    top: 356px;
  }
  .contact-row {
    display: flex;
    align-items: flex-start;
    gap: 34px;
    font-size: 22px;
    line-height: 34px;
    margin-bottom: 16px;
  }
  .contact-address { font-style: normal; }
  .contact-icon {
    width: 28px;
    height: 34px;
    flex: none;
  }
  .social {
    position: absolute;
    left: 99px;
    top: 626px;
    display: flex;
  }
  .social-item {
    display: flex;
    align-items: center;
    gap: 14px;
    font-size: 28px;
    color: var(--ink);
  }
  .social-item:nth-child(1) { width: 286px; }
  .social-item:nth-child(2) { width: 284px; }
  .social-mark {
    width: 40px;
    height: 40px;
    border-radius: 6px;
    background: var(--ink);
    flex: none;
  }
</style>
</head>
<body>
  <main class="card">
    <div class="photo-placeholder" role="img" aria-label="Photo of a latte with foam art in a cup, seen from above"></div>

    <p class="tagline">Your cup of inspiration.</p>

    <section class="contact">
      <div class="contact-row">
        <svg class="contact-icon" viewBox="0 0 28 34" aria-hidden="true">
          <path d="M14 4a8 8 0 0 0-8 8c0 6 8 16 8 16s8-10 8-16a8 8 0 0 0-8-8zm0 11a3 3 0 1 1 0-6 3 3 0 0 1 0 6z" fill="var(--ink)"/>
        </svg>
        <address class="contact-address">48 Harbor Lane,<br>Millbrook Bay, NY10482</address>
      </div>
      <div class="contact-row">
        <svg class="contact-icon" viewBox="0 0 28 34" aria-hidden="true">
          <path d="M9 5l5 1-1 7-4 1c0 4 2 8 5 10l3-2 5 5-3 4c-9-2-15-13-13-23z" fill="var(--ink)"/>
        </svg>
        <span>+555 010 2040</span>
      </div>
    </section>

    <footer class="social">
      <div class="social-item"><span class="social-mark"></span><span>rvcoffehouse</span></div>
      <div class="social-item"><span class="social-mark"></span><span>rvcoffehouse</span></div>
      <div class="social-item"><span class="social-mark"></span><span>rvcoffehouse.com</span></div>
    </footer>
  </main>
</body>
</html>
```